OLU58 biz card & Stationery

LU58 is a personalized shopping experience brought to you, that lets you find and discover fashion goods through a collection of boutiques curated by taste-makers - celebrities, stylists, designers, and fashion bloggers. Boutiques uses visual technology to help fashionistas discover and shop their look and creates the opportunity for designers to showcase their collections and latest inspirations online.

OLU58 is built on technology developed by our team of fashion experts who work with engineers to “teach” our computer systems to understand various patterns, pairings, and genre definitions. When signed into your account, OLU58 learns about your style and preferences and in turn, provides you better results and recommendations over time. Ultimately, OLU58 will provide shoppers with a much richer and interactive shopping experience and help drive traffic to retailers' websites.

We need a definitely cool business card. The card must be black! And must use our official logo which can be download from OLU58.com

The address for Letter head and evenlop, please use 4872 Crestwick Parkway, Sutie 510 Los Angeles CA90412, email will be anyone@OLU58.com, website is www.OLU58.com

thanks

We received some of the design, thanks. But most of the design are not what we want. We need a very clean version with black ground, you may also use some dark gray to add the element. please take a look at http://morvalstudio.no/work/#pelter__ostrama/, we do like this kind of design very much. hope it help.

```html
<!DOCTYPE html>
<html lang="en">
<head>
<meta charset="UTF-8">
<title>OLU58 Envelope</title>
<link rel="stylesheet" href="https://fonts.googleapis.com/css2?family=Tenor+Sans&display=swap">
<style>
  :root {
    --paper: #ffffff;
    --frame: #1a1a1a;
    --panel: #1f1f1f;
    --ink-light: #ffffff;
    --ink-muted: #8c8c8c;
    --band-edge: #2c2c2c;
    --band-mid: #3a3a3a;
  }
  html, body {
    margin: 0;
    padding: 0;
    width: 1200px;
    height: 862px;
    overflow: hidden;
    background: var(--paper);
  }
  .envelope {
    position: absolute;
    left: 75px;
    top: 54px;
    width: 1049px;
    height: 753px;
    border: 1px solid var(--frame);
    background: var(--paper);
  }
  .brand-panel {
    position: absolute;
    left: 0;
    top: 0;
    width: 481px;
    height: 100%;
    background: var(--panel);
    font-family: "Tenor Sans", "Optima", sans-serif;
  }
  .brand-name {
    position: absolute;
    left: 0;
    width: 478px;
    top: 76px;
    margin: 0;
    text-align: center;
    color: var(--ink-light);
    font-size: 74px;
    font-weight: 400;
    line-height: 1;
    letter-spacing: -0.5px;
  }
  .tagline {
    position: absolute;
    left: 0;
    width: 478px;
    top: 172px;
    margin: 0;
    text-align: center;
    color: var(--ink-muted);
    font-size: 19px;
    line-height: 1;
    letter-spacing: -0.3px;
  }
  .texture-band {
    position: absolute;
    left: 8px;
    top: 255px;
    width: 470px;
    height: 264px;
    background: linear-gradient(90deg, var(--band-edge), var(--band-mid) 50%, var(--band-edge));
  }
  .contact {
    position: absolute;
    left: 100px;
    top: 573px;
    margin: 0;
    color: var(--ink-light);
    font-size: 19px;
    line-height: 25.6px;
    font-style: normal;
  }
  .contact-label {
    display: inline-block;
    width: 31px;
    font-weight: 700;
  }
</style>
</head>
<body>
  <main class="envelope">
    <section class="brand-panel">
      <h1 class="brand-name">OLU58</h1>
      <p class="tagline">SOCIAL FASHION ONLINE</p>
      <div class="texture-band" role="img" aria-label="Decorative band of thin grey vertical pinstripes"></div>
      <address class="contact">
        4872 Crestwick Parkway,<br>
        Sutie 510<br>
        Los Angeles CA90412<br>
        <span class="contact-label">E</span>anyone@OLU58.com<br>
        <span class="contact-label">W</span>www.OLU58.com
      </address>
    </section>
  </main>
</body>
</html>
```